professional business card design

Business card design. Photos have been uploaded and i am open to the designer choosing which photos to use. Would like the card to be mostyly in a grey scale design with black, whites, silver & grey colours. I have added copy of our flyer as would like on the back side of card our services to be listed. Do not use any bright colurs such as blue red green or yellow. i need to be able to edit the phone number and naem in the final card design submitted.

Target Market(s)

Clients

Industry/Entity Type

earhmovibng and transport

Contact Information for Business Card

Director Name, address, email, phone number and services

Colors

Designer to choose only greyscale colors for use in the design.

Requirements
Should not have
• no yellow, red, blue or green

```html
<!DOCTYPE html>
<html lang="en">
<head>
<meta charset="utf-8">
<title>Halvern Haulage – Business Card</title>
<link href="https://fonts.googleapis.com/css2?family=Roboto+Condensed:ital,wght@0,400;0,700;1,700&display=swap" rel="stylesheet">
<style>
  :root{
    --page:#e6e7e8;
    --card:#0d0d0e;
    --card-mid:#1c1d1f;
    --steel:#3a3c3f;
    --silver:#c9cbce;
    --silver-light:#f1f2f3;
    --white:#ffffff;
    --muted:#a9abae;
  }
  *{box-sizing:border-box;margin:0;padding:0}
  html,body{width:885px;height:1200px;overflow:hidden}
  body{
    background:var(--page);
    font-family:"Roboto Condensed",Arial,sans-serif;
    position:relative;
  }
  .card{
    position:absolute;left:52px;width:780px;height:446px;
    border-radius:18px;overflow:hidden;
    background:var(--card);
    box-shadow:0 10px 28px rgba(0,0,0,.28);
  }
  .card--front{top:118px}
  .card--back{top:636px}

  /* front */
  .front-texture{
    position:absolute;left:0;top:0;width:100%;height:62%;
    background:radial-gradient(ellipse at 50% 35%,var(--steel) 0%,var(--card-mid) 55%,var(--card) 100%);
  }
  .front-swoosh{position:absolute;left:0;top:0;width:100%;height:100%}
  .brand{
    position:absolute;display:flex;align-items:center;gap:14px;
    color:var(--silver-light);font-weight:700;text-transform:uppercase;white-space:nowrap;
  }
  .brand__dot{flex:none;background:var(--silver);border-radius:50%}
  .card--front .brand{left:0;right:0;top:104px;justify-content:center;font-size:50px;letter-spacing:3px}
  .card--front .brand__dot{width:30px;height:30px}
  .holder-name{
    position:absolute;left:64px;top:272px;
    color:var(--white);font-size:42px;font-weight:700;letter-spacing:1px;
  }
  .contacts{
    position:absolute;left:64px;right:40px;top:340px;
    display:grid;grid-template-columns:1fr 1fr;row-gap:18px;column-gap:24px;
  }
  .contact{display:flex;align-items:center;gap:12px;color:var(--silver);font-size:17px;line-height:1.15}
  .contact__icon{
    flex:none;width:30px;height:30px;border-radius:4px;background:var(--silver);
    display:flex;align-items:center;justify-content:center;
  }
  .contact__icon svg{width:18px;height:18px;fill:var(--card)}

  /* back */
  .back-photo{
    position:absolute;left:0;top:150px;width:52%;height:296px;
    background:linear-gradient(160deg,#55585c 0%,#2b2c2e 55%,#111 100%);
  }
  .back-photo::after{
    content:"";position:absolute;inset:0;
    background:linear-gradient(90deg,transparent 60%,var(--card) 100%),
               linear-gradient(180deg,var(--card) 0%,transparent 25%);
  }
  .card--back .brand{left:36px;top:36px;font-size:30px;letter-spacing:1.5px;gap:10px}
  .card--back .brand__dot{width:20px;height:20px}
  .services-title{
    position:absolute;left:36px;top:86px;
    color:var(--white);font-size:22px;font-weight:700;font-style:italic;text-transform:uppercase;
    letter-spacing:1px;
  }
  .services{
    position:absolute;left:430px;top:30px;right:20px;list-style:none;
  }
  .services li{
    display:flex;align-items:flex-start;gap:10px;
    color:var(--white);font-size:21px;font-weight:700;font-style:italic;line-height:1.1;
    margin-bottom:7px;
  }
  .services svg{flex:none;width:16px;height:16px;margin-top:4px;fill:var(--silver)}
</style>
</head>
<body>

<section class="card card--front" aria-label="Business card front">
  <div class="front-texture"></div>
  <svg class="front-swoosh" viewBox="0 0 780 446" preserveAspectRatio="none" aria-hidden="true">
    <defs>
      <linearGradient id="silverBand" x1="0" y1="0" x2="1" y2="0">
        <stop offset="0" stop-color="#6f7276"/>
        <stop offset=".5" stop-color="#f1f2f3"/>
        <stop offset="1" stop-color="#6f7276"/>
      </linearGradient>
    </defs>
    <path d="M0 238 Q390 200 780 238 L780 276 Q390 236 0 276 Z" fill="var(--card)"/>
    <path d="M0 238 Q390 200 780 238 L780 244 Q390 208 0 244 Z" fill="url(#silverBand)"/>
    <path d="M0 244 Q390 208 780 244 L780 446 L0 446 Z" fill="var(--card)"/>
  </svg>

  <div class="brand"><span class="brand__dot"></span>Halvern Haulage</div>

  <h1 class="holder-name">NAME SURNAME</h1>

  <div class="contacts">
    <div class="contact">
      <span class="contact__icon"><svg viewBox="0 0 24 24"><path d="M6.6 10.8a15 15 0 0 0 6.6 6.6l2.2-2.2c.3-.3.7-.4 1-.2 1.1.4 2.3.6 3.6.6.6 0 1 .4 1 1V20c0 .6-.4 1-1 1A17 17 0 0 1 3 4c0-.6.4-1 1-1h3.5c.6 0 1 .4 1 1 0 1.3.2 2.5.6 3.6.1.3 0 .7-.2 1z"/></svg></span>
      +61 400 555 018
    </div>
    <div class="contact">
      <span class="contact__icon"><svg viewBox="0 0 24 24"><path d="M3 5h18v14H3zm2 2v.4l7 4.6 7-4.6V7zm0 2.8V17h14V9.8l-7 4.6z"/></svg></span>
      office@halvernhaulage.com
    </div>
    <div class="contact">
      <span class="contact__icon"><svg viewBox="0 0 24 24"><path d="M12 2a7 7 0 0 0-7 7c0 5.2 7 13 7 13s7-7.8 7-13a7 7 0 0 0-7-7zm0 9.5A2.5 2.5 0 1 1 12 6.5a2.5 2.5 0 0 1 0 5z"/></svg></span>
      18 Quarry Lane,<br>Ridgeford NSW 2790
    </div>
    <div class="contact">
      <span class="contact__icon"><svg viewBox="0 0 24 24"><path d="M12 2a10 10 0 1 0 0 20 10 10 0 0 0 0-20zm6.9 6h-3a15 15 0 0 0-1.3-3.6A8 8 0 0 1 18.9 8zM12 4c.8 1.2 1.5 2.5 1.9 4h-3.8c.4-1.5 1.1-2.8 1.9-4zM4.3 14a8 8 0 0 1 0-4h3.4a16 16 0 0 0 0 4zm.8 2h3a15 15 0 0 0 1.3 3.6A8 8 0 0 1 5.1 16zm3-8h-3a8 8 0 0 1 4.3-3.6C8.8 5.5 8.4 6.7 8.1 8zM12 20c-.8-1.2-1.5-2.5-1.9-4h3.8c-.4 1.5-1.1 2.8-1.9 4zm2.3-6H9.7a14 14 0 0 1 0-4h4.6a14 14 0 0 1 0 4zm.3 5.6c.6-1.1 1-2.3 1.3-3.6h3a8 8 0 0 1-4.3 3.6zm1.7-5.6a16 16 0 0 0 0-4h3.4a8 8 0 0 1 0 4z"/></svg></span>
      www.halvernhaulage.com
    </div>
  </div>
</section>

<section class="card card--back" aria-label="Business card back">
  <div class="back-photo" role="img" aria-label="Photo of a heavy haulage truck carrying earthmoving equipment"></div>

  <div class="brand"><span class="brand__dot"></span>Halvern Haulage</div>
  <h2 class="services-title">Our Services</h2>

  <ul class="services">
    <li><svg viewBox="0 0 16 16"><path d="M3 1l7 7-7 7h4l7-7-7-7z"/></svg>Over Size Loads / Hot Shot Loads</li>
    <li><svg viewBox="0 0 16 16"><path d="M3 1l7 7-7 7h4l7-7-7-7z"/></svg>Heavy Vehicle Recovery Services</li>
    <li><svg viewBox="0 0 16 16"><path d="M3 1l7 7-7 7h4l7-7-7-7z"/></svg>Potable Water Deliveries</li>
    <li><svg viewBox="0 0 16 16"><path d="M3 1l7 7-7 7h4l7-7-7-7z"/></svg>Road Building / Maintenance</li>
    <li><svg viewBox="0 0 16 16"><path d="M3 1l7 7-7 7h4l7-7-7-7z"/></svg>Earthworks</li>
    <li><svg viewBox="0 0 16 16"><path d="M3 1l7 7-7 7h4l7-7-7-7z"/></svg>Sand &amp; Metal Supply &amp; Cartage</li>
    <li><svg viewBox="0 0 16 16"><path d="M3 1l7 7-7 7h4l7-7-7-7z"/></svg>Road Train Tippers</li>
    <li><svg viewBox="0 0 16 16"><path d="M3 1l7 7-7 7h4l7-7-7-7z"/></svg>Road Train Tankers</li>
    <li><svg viewBox="0 0 16 16"><path d="M3 1l7 7-7 7h4l7-7-7-7z"/></svg>Road Train Flat Tops</li>
    <li><svg viewBox="0 0 16 16"><path d="M3 1l7 7-7 7h4l7-7-7-7z"/></svg>Prog Rock Trailers</li>
    <li><svg viewBox="0 0 16 16"><path d="M3 1l7 7-7 7h4l7-7-7-7z"/></svg>Mine Site Accredited<br>Equipment &amp; Operators</li>
  </ul>
</section>

</body>
</html>
```